Open Door Dialogues: Classroom and Family Allies building brighter pupil futures.

This is a book that helps to prepare for and hold a standard conference that an educator would have with the parents of the students in the school. It is also about how to have problem-solving conferences around difficult issues using techniques from family therapy. Parent involvement is a key ingredient for student success, but most educators have no training in holding meetings with parents. This book fills that gap.

Target Market(s)

Teachers, principals, counselors, school psychologists, school nurses. Anyone who has conferences with the parents of their students.

Font styles to use
Sans Serif

Colors
85acd3
ffcf3e

Requirements
Must have
• I have several books coming up. I'd like something that could be carried over to the new ones without too many changes. They won't all be about education. I am a psychologist so most of my writings will cover subjects related to emotional intelligence.
Nice to have
• Something dignified that will pop out for those in the schools. I like the combination of a royal blue background with white and gold (not yellow) lettering.
Should not have
• I'd like it to be easy to read. Not too messy or too much stuff on the page.

```html
<!DOCTYPE html>
<html lang="en">
<head>
<meta charset="utf-8">
<title>Open Door Dialogues – Book Cover</title>
<link rel="stylesheet" href="https://fonts.googleapis.com/css2?family=Bebas+Neue&family=Montserrat:wght@500;600;800&display=swap">
<style>
  :root {
    --royal-navy: #0c2a63;
    --gold-light: #fbe7a1;
    --gold-mid: #f3d172;
    --gold-deep: #e9c25e;
    --white: #ffffff;
  }
  html, body {
    margin: 0;
    padding: 0;
    overflow: hidden;
    background: var(--royal-navy);
  }
  .cover {
    position: relative;
    width: 800px;
    height: 1200px;
    background: var(--royal-navy);
    overflow: hidden;
  }
  .title-line {
    position: absolute;
    left: 0;
    width: 800px;
    margin: 0;
    text-align: center;
    font-family: "Bebas Neue", "Arial Narrow", sans-serif;
    font-weight: 400;
    line-height: 1;
  }
  .title-gold {
    font-size: 300px;
    background: linear-gradient(120deg, var(--gold-mid) 0%, var(--gold-light) 30%, var(--gold-deep) 55%, var(--gold-light) 80%, var(--gold-mid) 100%);
    -webkit-background-clip: text;
    background-clip: text;
    color: transparent;
  }
  .title-open { top: -6px; }
  .title-door { top: 262px; }
  .title-white {
    top: 548px;
    font-size: 156px;
    color: var(--white);
    letter-spacing: 1px;
  }
  .subtitle {
    position: absolute;
    left: 0;
    width: 800px;
    text-align: center;
    font-family: "Montserrat", Arial, sans-serif;
    text-transform: uppercase;
  }
  .subtitle-line {
    position: absolute;
    left: 0;
    width: 800px;
    font-weight: 500;
    font-size: 33px;
    letter-spacing: 4px;
    color: var(--white);
    line-height: 1;
  }
  .subtitle-line .small-word { font-size: 25px; }
  .subtitle-top { top: 772px; }
  .subtitle-bottom { top: 900px; }
  .highlight-band {
    position: absolute;
    left: 140px;
    top: 822px;
    width: 520px;
    height: 58px;
    background: linear-gradient(90deg, var(--gold-mid), var(--gold-light) 45%, var(--gold-mid));
    color: var(--royal-navy);
    font-weight: 800;
    font-size: 28px;
    letter-spacing: 3px;
    line-height: 58px;
  }
  .author-name {
    position: absolute;
    left: 0;
    top: 1062px;
    width: 800px;
    margin: 0;
    text-align: center;
    font-family: "Bebas Neue", "Arial Narrow", sans-serif;
    font-weight: 400;
    font-size: 88px;
    line-height: 1;
    letter-spacing: 30px;
    padding-left: 30px;
    box-sizing: border-box;
    color: var(--white);
  }
</style>
</head>
<body>
  <main class="cover">
    <h1 class="book-title">
      <span class="title-line title-gold title-open">Open</span>
      <span class="title-line title-gold title-door">Door</span>
      <span class="title-line title-white">Dialogues</span>
    </h1>
    <div class="subtitle">
      <div class="subtitle-line subtitle-top">Classroom <span class="small-word">and</span> Family Allies</div>
      <div class="highlight-band">Building Brighter</div>
      <div class="subtitle-line subtitle-bottom">Pupil Futures</div>
    </div>
    <p class="author-name">Author Name</p>
  </main>
</body>
</html>
```